Pellmont Industries Line Card

Hello - We're looking to develop a two sided brochure for our company product lines and capabilities. We're a distributor, value-added reseller, we build cable assemblies and panel assemblies. Looking for a flyer to help tell our story. Our primary market is selling to customers in the off-highway equipment markets. Construction, AG and Specialty Vehicles.

```html
<!DOCTYPE html>
<html lang="en">
<head>
<meta charset="utf-8">
<title>Pellmont Industries Line Card</title>
<link href="https://fonts.googleapis.com/css2?family=Poppins:wght@400;500;600;700&family=Roboto+Condensed:wght@700&display=swap" rel="stylesheet">
<style>
:root{
  --navy:#252e5c;
  --red:#e3262b;
  --ink:#1d1d1f;
  --white:#ffffff;
  --stage:#f2f2f3;
  --orange:#e79a2b;
}
*{margin:0;padding:0;box-sizing:border-box}
html,body{width:882px;height:1200px;overflow:hidden;background:var(--stage)}
.sheet{position:relative;width:882px;height:1200px;overflow:hidden}
.page{position:absolute;top:294px;width:810px;height:1150px;background:var(--white);font-family:'Poppins',sans-serif;overflow:hidden;transform:scale(.532);transform-origin:0 0}
.page-front{left:0}
.page-back{left:451px}
.layer{position:absolute;left:0;top:0}
.brand{position:absolute;top:34px;width:338px}
.page-front .brand{left:30px}
.page-back .brand{left:440px}
.brand-name{display:flex;align-items:center;justify-content:flex-end;gap:12px;font-weight:700;font-size:56px;color:var(--navy);line-height:1}
.brand-name .mark{width:22px;height:22px;background:var(--navy)}
.brand-bar{margin-top:14px;background:var(--navy);color:var(--white);font-family:'Roboto Condensed',sans-serif;font-weight:700;font-size:19px;text-align:right;padding:1px 14px 1px 0}
.tagline{margin-top:8px;font-weight:600;font-size:16.5px;line-height:1.3;color:var(--ink);text-align:right}
.tagline .accent{color:var(--red)}
.product-top{position:absolute;left:505px;top:12px;width:255px;height:124px;border-radius:6px;background:linear-gradient(90deg,#c7b8a5,#3b3a3a 50%,#b9a989)}
.list{position:absolute;list-style:none;color:var(--white);line-height:26.8px}
.list li{display:flex;align-items:center;gap:8px;white-space:nowrap}
.list li::before{content:"";width:13px;height:10px;border:1.5px solid #d8dbe6;border-radius:1px;flex:none}
.list-left{left:35px;top:292px;font-size:19px}
.list-right{left:472px;top:185px;font-size:18.5px}
.partners{position:absolute;left:58px;width:694px;display:flex;align-items:center;justify-content:space-between;font-weight:700;font-size:22px;color:var(--navy)}
.page-front .partners{top:950px}
.page-back .partners{top:946px}
.partners .p-red{color:var(--red)}
.partners .p-orange{color:var(--orange);font-weight:600;font-size:17px}
.partners .p-dot{display:inline-block;width:14px;height:14px;border-radius:50%;background:var(--navy);margin-right:6px;vertical-align:middle}
.rule{position:absolute;left:135px;top:1008px;width:585px;height:3px;background:var(--navy);border-radius:2px}
.contact{position:absolute;left:0;width:810px;text-align:center}
.phone{top:1026px;font-weight:600;font-size:19px;color:var(--navy)}
.phone .label{font-size:15px}
.web{top:1055px;font-weight:600;font-size:20px;letter-spacing:5px;color:var(--ink)}
.page-back .phone,.page-back .web{color:var(--white)}
</style>
</head>
<body>
<main class="sheet">

  <section class="page page-front" aria-label="Front side">
    <svg class="layer" width="810" height="1150" viewBox="0 0 810 1150">
      <polygon points="0,290 400,180 400,172 810,100 810,822 0,862" fill="var(--navy)"/>
      <path d="M0,1140 Q405,1128 810,1140 L810,1150 L0,1150 Z" fill="var(--navy)"/>
    </svg>

    <header class="brand">
      <div class="brand-name"><span class="mark"></span>Pellmont</div>
      <div class="brand-bar">Pellmont Industries</div>
      <p class="tagline">Distribution, Contract Manufacturing,<br><span class="accent">and System Integration</span></p>
    </header>

    <div class="product-top" role="img" aria-label="Product photo of three rotary cam switches"></div>

    <ul class="list list-left">
      <li>Power Distribution Modules</li><li>Circuit Breakers, Fuses</li><li>rocker &amp; Toggle Switches</li>
      <li>CAN Switches</li><li>Battery Disconnects</li><li>Battery Equalizers</li><li>Power Converters</li>
      <li>True Sine Wave Inverters</li><li>Battery Separators</li><li>Interconnect Controllers</li>
      <li>Battery Isolators</li><li>Custom Assemblies</li><li>Wire Harnesses</li><li>Testing</li>
      <li>Product Integration</li><li>Custon Bus Bars</li><li>Kitting</li>
    </ul>

    <ul class="list list-right">
      <li>On Vehicle &amp; Mobile</li><li>Equipment Display</li><li>HMIs Displays SCADA Software</li>
      <li>HMI + PLC Hybrids</li><li>Automation Cables Connectors</li><li>Passive Distributors</li>
      <li>DIN Valve Connectors</li><li>Industrial Ethernet/Connectors</li><li>Fuse Blocks , Fuse Holders</li>
      <li>Circuit Breakers</li><li>Resettable Fuses</li><li>Fuse Accessories</li>
    </ul>

    <svg class="layer" width="810" height="1150" viewBox="0 0 810 1150">
      <defs>
        <linearGradient id="frame" x1="0" y1="0" x2="1" y2="1">
          <stop offset="0" stop-color="#e3262b"/><stop offset="1" stop-color="#3a2150"/>
        </linearGradient>
        <linearGradient id="photo-grey" x1="0" y1="0" x2="1" y2="1">
          <stop offset="0" stop-color="#d9d6d2"/><stop offset="1" stop-color="#8d8a88"/>
        </linearGradient>
        <linearGradient id="photo-green" x1="0" y1="0" x2="1" y2="1">
          <stop offset="0" stop-color="#2b2b2b"/><stop offset="1" stop-color="#6fcf76"/>
        </linearGradient>
        <linearGradient id="photo-red" x1="0" y1="0" x2="1" y2="1">
          <stop offset="0" stop-color="#e8562d"/><stop offset="1" stop-color="#cfcfcf"/>
        </linearGradient>
        <linearGradient id="photo-switch" x1="0" y1="0" x2="1" y2="1">
          <stop offset="0" stop-color="#f2f2f2"/><stop offset="0.5" stop-color="#2a2a2a"/><stop offset="1" stop-color="#cfd6e4"/>
        </linearGradient>
        <linearGradient id="photo-panel" x1="0" y1="0" x2="1" y2="1">
          <stop offset="0" stop-color="#3e4a66"/><stop offset="1" stop-color="#9fa7b5"/>
        </linearGradient>
      </defs>
      <g stroke="url(#frame)" stroke-width="7">
        <polygon role="img" aria-label="Photo of a wire lead assembly" points="385,257 430,283 430,335 385,361 340,335 340,283" fill="url(#photo-grey)"/>
        <polygon role="img" aria-label="Photo of a control box with switch" points="385,378 430,404 430,456 385,482 340,456 340,404" fill="url(#photo-grey)"/>
        <polygon role="img" aria-label="Photo of green terminal block connectors" points="385,495 430,521 430,573 385,599 340,573 340,521" fill="url(#photo-green)"/>
        <polygon role="img" aria-label="Photo of a red battery disconnect switch" points="385,608 430,634 430,686 385,712 340,686 340,634" fill="url(#photo-red)"/>
        <polygon role="img" aria-label="Photo of an operator display panel" points="283,695 387,755 387,875 283,935 179,875 179,755" fill="url(#photo-panel)" stroke-width="9"/>
        <polygon role="img" aria-label="Photo of a key operated rotary switch" points="650,525 828,627 828,833 650,935 472,833 472,627" fill="url(#photo-switch)" stroke-width="14"/>
      </g>
    </svg>

    <div class="partners">
      <span>Varden</span>
      <span><span class="p-dot"></span>Fuselane</span>
      <span>Kestrel</span>
      <span class="p-red">Orvik</span>
      <span class="p-orange">Halden Automation</span>
    </div>
    <div class="rule"></div>
    <p class="contact phone">(555)014-2290 <span class="label">FAX:</span> (555) 014-2291</p>
    <p class="contact web">www.pellmontindustries.com</p>
  </section>

  <section class="page page-back" aria-label="Back side">
    <svg class="layer" width="810" height="1150" viewBox="0 0 810 1150">
      <defs>
        <linearGradient id="tile-a" x1="0" y1="0" x2="1" y2="1"><stop offset="0" stop-color="#d9453f"/><stop offset="1" stop-color="#6b6560"/></linearGradient>
        <linearGradient id="tile-b" x1="0" y1="0" x2="1" y2="1"><stop offset="0" stop-color="#3b4a78"/><stop offset="1" stop-color="#b8a68f"/></linearGradient>
        <linearGradient id="tile-c" x1="0" y1="0" x2="1" y2="1"><stop offset="0" stop-color="#c9c7c0"/><stop offset="1" stop-color="#a9923a"/></linearGradient>
        <linearGradient id="tile-d" x1="0" y1="0" x2="1" y2="1"><stop offset="0" stop-color="#c7b49a"/><stop offset="1" stop-color="#8e8a86"/></linearGradient>
        <linearGradient id="tile-e" x1="0" y1="0" x2="1" y2="1"><stop offset="0" stop-color="#d2bf9b"/><stop offset="1" stop-color="#9a8a73"/></linearGradient>
        <linearGradient id="tile-f" x1="0" y1="0" x2="1" y2="1"><stop offset="0" stop-color="#cfc2ae"/><stop offset="1" stop-color="#3a3a3a"/></linearGradient>
        <linearGradient id="tile-g" x1="0" y1="0" x2="1" y2="1"><stop offset="0" stop-color="#b9bcc2"/><stop offset="1" stop-color="#55585f"/></linearGradient>
        <linearGradient id="tile-h" x1="0" y1="0" x2="1" y2="1"><stop offset="0" stop-color="#d9cf5a"/><stop offset="1" stop-color="#a7a7a7"/></linearGradient>
        <linearGradient id="tile-i" x1="0" y1="0" x2="1" y2="1"><stop offset="0" stop-color="#2a2e2c"/><stop offset="1" stop-color="#d33a44"/></linearGradient>
      </defs>
      <polygon points="0,100 408,180 810,285 810,930 0,930" fill="var(--navy)"/>
      <rect x="0" y="995" width="810" height="155" fill="var(--navy)"/>
      <g fill="none" stroke="var(--white)" stroke-width="2.5">
        <rect x="75" y="233" width="190" height="180" rx="16"/>
        <rect x="322" y="233" width="190" height="180" rx="16"/>
        <rect x="565" y="233" width="190" height="180" rx="16"/>
        <rect x="75" y="468" width="190" height="180" rx="16"/>
        <rect x="322" y="468" width="190" height="180" rx="16"/>
        <rect x="565" y="468" width="190" height="180" rx="16"/>
        <rect x="75" y="698" width="190" height="180" rx="16"/>
        <rect x="322" y="698" width="190" height="180" rx="16"/>
        <rect x="565" y="698" width="190" height="180" rx="16"/>
      </g>
      <rect role="img" aria-label="Photo of a battery terminal block with red cover" x="65" y="245" width="190" height="180" rx="14" fill="url(#tile-a)"/>
      <rect role="img" aria-label="Photo of a wired relay assembly" x="312" y="245" width="190" height="180" rx="14" fill="url(#tile-b)"/>
      <rect role="img" aria-label="Photo of an enclosure with terminal strip" x="555" y="245" width="190" height="180" rx="14" fill="url(#tile-c)"/>
      <rect role="img" aria-label="Photo of a row of red rocker switches" x="65" y="480" width="190" height="180" rx="14" fill="url(#tile-d)"/>
      <rect role="img" aria-label="Photo of a wire harness on an assembly board" x="312" y="480" width="190" height="180" rx="14" fill="url(#tile-e)"/>
      <rect role="img" aria-label="Photo of a cable junction box" x="555" y="480" width="190" height="180" rx="14" fill="url(#tile-f)"/>
      <rect role="img" aria-label="Photo of a wired control panel" x="65" y="710" width="190" height="180" rx="14" fill="url(#tile-g)"/>
      <rect role="img" aria-label="Photo of terminal blocks with yellow markers" x="312" y="710" width="190" height="180" rx="14" fill="url(#tile-h)"/>
      <rect role="img" aria-label="Photo of red wiring inside a cabinet" x="555" y="710" width="190" height="180" rx="14" fill="url(#tile-i)"/>
    </svg>

    <header class="brand">
      <div class="brand-name"><span class="mark"></span>Pellmont</div>
      <div class="brand-bar">Pellmont Industries</div>
      <p class="tagline">Distribution, Contract Manufacturing,<br><span class="accent">and System Integration</span></p>
    </header>

    <div class="partners">
      <span>Varden</span>
      <span><span class="p-dot"></span>Fuselane</span>
      <span>Kestrel</span>
      <span class="p-red">Orvik</span>
      <span class="p-orange">Halden Automation</span>
    </div>
    <p class="contact phone">(555)014-2290 <span class="label">FAX:</span> (555) 014-2291</p>
    <p class="contact web">www.pellmontindustries.com</p>
  </section>

</main>
</body>
</html>
```